Create a website in Wordpress for an interior design company

Create a website for our interior design company 'Dwellora'

-Color preferences - Neutral and warm colors. Nothing too bright
-Aesthetic: Modern, Minimalist, Classic, Mature, Luxury
-Mission Statement: Transforming homes into personalized dream spaces through exceptional interior design, meticulous attention to detail, and a touch of the unexpected.
-Brand Values: innovation, creativity, passion and sustainability

Examples: https://www.petrakinslowinteriors.com.au/
https://www.tavelcraftstudio.com/

About
Portfolio
Inquire page

```html
<!DOCTYPE html>
<html lang="en">
<head>
<meta charset="utf-8">
<title>Dwellora — Interior Design</title>
<link rel="stylesheet" href="https://fonts.googleapis.com/css2?family=Poppins:wght@300;400;500;600&display=swap">
<style>
:root{
  --gold:#d8bc80;
  --gold-deep:#d1ad6b;
  --cream:#fdfaf5;
  --sand:#f1e8da;
  --ink:#2c2a28;
  --text:#2b2b2b;
  --footer:#dcc186;
  --white:#ffffff;
}
*{margin:0;padding:0;box-sizing:border-box}
html,body{width:1200px;height:4071px;overflow:hidden}
body{position:relative;background:var(--white);font-family:'Poppins',sans-serif;color:var(--text)}
.abs{position:absolute}

/* header */
.site-header{left:0;top:0;width:1200px;height:152px;background:var(--cream)}
.brand{left:63px;top:48px;font-size:52px;font-weight:400;color:var(--gold);letter-spacing:.5px}
.nav-link{top:77px;font-size:14px;color:#333}
.nav-link.active::after{content:"";position:absolute;left:0;right:0;top:26px;height:2px;background:var(--gold)}
.inquire-btn{left:994px;top:66px;width:98px;height:40px;border:2px solid var(--gold);border-radius:20px;font-size:14px;text-align:center;line-height:36px;color:#333}

/* hero */
.hero-photo{left:0;top:152px;width:1200px;height:596px;background:linear-gradient(100deg,#d9cbb0 0%,#efe6d3 30%,#f6efe2 55%,#e8d7b6 78%,#cdb78f 100%)}
.hero-card{left:66px;top:297px;width:715px;height:309px;background:rgba(255,255,255,.55);border-radius:8px}
.hero-kicker{left:74px;top:312px;font-size:46px;font-weight:600;color:#333}
.hero-title{left:72px;top:370px;font-size:82px;font-weight:600;color:#2b2b2b;line-height:1.1}
.hero-text{left:77px;top:476px;width:650px;font-size:15.5px;line-height:18px;color:#333}
.pill{background:var(--gold);color:var(--white);border-radius:30px;text-align:center}
.hero-btn{left:76px;top:534px;width:114px;height:30px;font-size:14px;line-height:30px}

/* about */
.about-frame{left:93px;top:819px;width:435px;height:691px;background:var(--sand)}
.about-photo{left:141px;top:860px;width:476px;height:610px;background:linear-gradient(160deg,#3d3632 0%,#2a2624 45%,#5a4634 75%,#8a7a66 100%)}
.section-title{font-size:46px;font-weight:400;color:var(--gold-deep)}
.about-title{left:670px;top:928px}
.about-text{left:670px;top:1020px;width:416px;font-size:15.6px;line-height:20px;text-align:justify;color:#222;hyphens:auto;-webkit-hyphens:auto}
.about-btn{left:670px;top:1336px;width:149px;height:51px;font-size:16px;line-height:51px}

/* portfolio */
.portfolio{left:0;top:1605px;width:1200px;height:1067px;background:var(--cream)}
.portfolio-title{left:0;width:1200px;top:1662px;text-align:center}
.shot{border-radius:5px}
.view-btn{left:512px;top:2541px;width:173px;height:52px;font-size:21px;line-height:52px}

/* contact */
.contact{left:0;top:2672px;width:1200px;height:865px;background:linear-gradient(180deg,#2f2d2c 0%,#353230 50%,#2e2b29 100%)}
.contact-title{left:0;width:1200px;top:2748px;text-align:center}
.field{background:var(--white);font-size:21px;color:#9a9a9a;padding:22px 13px}
.submit-btn{left:528px;top:3410px;width:134px;height:43px;font-size:21px;line-height:43px}

/* footer */
.site-footer{left:0;top:3537px;width:1200px;height:534px;background:var(--footer)}
.footer-brand{left:88px;top:3758px;font-size:48px;color:var(--white)}
.footer-head{top:3652px;font-size:22px;font-weight:500;color:var(--white)}
.footer-rule{top:3700px;height:2px;background:var(--white);width:60px}
.footer-link{left:384px;font-size:16px;color:var(--white)}
.footer-link::before{content:"";position:absolute;left:-18px;top:9px;width:6px;height:6px;border-radius:50%;background:var(--white)}
.footer-item{left:610px;font-size:16px;line-height:24px;color:var(--white)}
.footer-item b{font-weight:500}
.icon{left:566px}
.news-text{left:838px;top:3736px;width:300px;font-size:15px;line-height:26px;color:var(--white)}
.news-input{left:833px;top:3802px;width:302px;height:51px;background:var(--white);border-radius:26px;font-size:15px;color:#aaa;padding:14px 22px}
.subscribe-btn{left:833px;top:3867px;width:92px;height:27px;background:var(--white);border-radius:14px;font-size:12px;color:var(--gold);text-align:center;line-height:27px}
.social{width:48px;height:48px;border-radius:50%;border:2px solid var(--white);top:3902px}
.footer-line{left:68px;top:3987px;width:1067px;height:1px;background:var(--white)}
.copyright{left:0;width:1200px;top:4008px;text-align:center;font-size:13px;color:var(--white)}
</style>
</head>
<body>

<header class="abs site-header"></header>
<div class="abs brand">Dwellora</div>
<nav>
  <a class="abs nav-link active" style="left:542px">Home</a>
  <a class="abs nav-link" style="left:639px">About Us</a>
  <a class="abs nav-link" style="left:759px">Portfolio</a>
  <a class="abs nav-link" style="left:879px">Contact</a>
  <a class="abs inquire-btn">Inquire</a>
</nav>

<section>
  <div class="abs hero-photo" role="img" aria-label="Bright modern living room with staircase, framed art and warm ceiling lights"></div>
  <div class="abs hero-card"></div>
  <h2 class="abs hero-kicker">Welcome to</h2>
  <h1 class="abs hero-title">Dwellora</h1>
  <p class="abs hero-text">Lorem ipsum dolor sit amet, consectetur adipiscing elit, sed do eiusmod tempor in-cididunt ut labore et dolore magna aliqua. Quis ipsum suspendisse ultrices gravi-</p>
  <a class="abs pill hero-btn">Read More</a>
</section>

<section>
  <div class="abs about-frame"></div>
  <div class="abs about-photo" role="img" aria-label="Dark dining room with round table, upholstered chairs, wood slat walls and pendant lamps"></div>
  <h2 class="abs section-title about-title">About Us</h2>
  <p class="abs about-text">Lorem ipsum dolor sit amet, consectetur adipiscing elit, sed do eiusmod tempor incididunt ut labore et dolore magna aliqua. Quis ipsum suspendisse ultrices gravida. Risus commodo viverra maecenas accumsan lacus vel facilisis.Lorem ipsum dolor sit amet, consectetur adipiscing elit, sed do eiusmod tempor incididunt ut labore et dolore magna aliqua. Ut enim ad minim veniam, quis nostrud exercitation ullamco laboris nisi ut aliquip ex ea commodo consequat. Duis aute irure dolor in reprehenderit in voluptate velit esse cillum dolore eu fugiat nulla pariatur. Excepteur sint occaecat cupidatat non proident, sunt in culpa qui officia deserunt mollit anim id est laborum.</p>
  <a class="abs pill about-btn">Read More</a>
</section>

<section class="abs portfolio"></section>
<h2 class="abs section-title portfolio-title">Portfolio</h2>
<div class="abs shot" style="left:88px;top:1774px;width:320px;height:302px;background:linear-gradient(160deg,#4a4540,#8c8276 45%,#c9bfae 70%,#6b5a45)" role="img" aria-label="Living room with cream sofa and shelving"></div>
<div class="abs shot" style="left:446px;top:1774px;width:327px;height:362px;background:linear-gradient(170deg,#f2f1ee,#e2dfd8 55%,#8a8076 85%,#5b4f44)" role="img" aria-label="White entry hall with large pendant and plant"></div>
<div class="abs shot" style="left:803px;top:1774px;width:320px;height:302px;background:linear-gradient(120deg,#efe7dc,#d9c6a8 45%,#9db38a 75%,#6e8f5a)" role="img" aria-label="Dining area with round table beside garden window"></div>
<div class="abs shot" style="left:95px;top:2123px;width:313px;height:361px;background:linear-gradient(150deg,#3e434f,#c9b896 40%,#2f5e8c 70%,#6b5344)" role="img" aria-label="Dining room with blue chairs and brass chandelier"></div>
<div class="abs shot" style="left:446px;top:2183px;width:324px;height:301px;background:linear-gradient(150deg,#e9dcc8,#c9a57c 50%,#8a6642 80%,#5e4632)" role="img" aria-label="Reading nook with armchair and wall shelves"></div>
<div class="abs shot" style="left:805px;top:2123px;width:318px;height:361px;background:linear-gradient(140deg,#e7dfd2,#b88457 45%,#efe6d6 70%,#c8a766)" role="img" aria-label="Lounge with wood slat ceiling and white armchairs"></div>
<a class="abs pill view-btn">View More</a>

<section class="abs contact" role="img" aria-label="Dim interior backdrop with hanging bulbs"></section>
<h2 class="abs section-title contact-title">Contact Us</h2>
<div class="abs field" style="left:149px;top:2871px;width:430px;height:74px">First Name</div>
<div class="abs field" style="left:618px;top:2871px;width:430px;height:74px">Email</div>
<div class="abs field" style="left:149px;top:3006px;width:430px;height:74px">Phone Number</div>
<div class="abs field" style="left:618px;top:3006px;width:430px;height:74px">Inquire</div>
<div class="abs field" style="left:149px;top:3140px;width:899px;height:234px">Message</div>
<a class="abs pill submit-btn">Submit</a>

<footer class="abs site-footer"></footer>
<div class="abs footer-brand">Dwellora</div>

<h3 class="abs footer-head" style="left:362px">LINKS</h3>
<div class="abs footer-rule" style="left:362px"></div>
<a class="abs footer-link" style="top:3732px">About Us</a>
<a class="abs footer-link" style="top:3778px">Portfolio</a>
<a class="abs footer-link" style="top:3824px">Contact</a>

<h3 class="abs footer-head" style="left:566px">CONTACT US</h3>
<div class="abs footer-rule" style="left:566px"></div>
<svg class="abs icon" style="top:3738px" width="30" height="30" viewBox="0 0 30 30"><circle cx="15" cy="15" r="14" fill="#fff"/><path d="M15 7a5 5 0 0 0-5 5c0 4 5 10 5 10s5-6 5-10a5 5 0 0 0-5-5zm0 7a2 2 0 1 1 0-4 2 2 0 0 1 0 4z" fill="var(--footer)"/></svg>
<div class="abs footer-item" style="top:3728px"><b>ADDRESS:</b><br>2215 N Elmwood Ln,<br>Brookdale, FL 32907</div>
<svg class="abs icon" style="top:3826px" width="30" height="30" viewBox="0 0 30 30"><circle cx="15" cy="15" r="14" fill="#fff"/><path d="M10 8l3 0 1 4-2 1.5a9 9 0 0 0 4.5 4.5L18 16l4 1v3c0 1-1 2-2 2A12 12 0 0 1 8 10c0-1 1-2 2-2z" fill="var(--footer)"/></svg>
<div class="abs footer-item" style="top:3818px"><b>PHONE:</b><br>+39 0420 555 018</div>
<svg class="abs icon" style="top:3896px" width="30" height="30" viewBox="0 0 30 30"><circle cx="15" cy="15" r="14" fill="#fff"/><rect x="8" y="10" width="14" height="10" rx="1.5" fill="none" stroke="var(--footer)" stroke-width="2"/><path d="M8.5 11l6.5 5 6.5-5" fill="none" stroke="var(--footer)" stroke-width="2"/></svg>
<div class="abs footer-item" style="top:3888px"><b>EMAIL:</b><br>hello@dwellora-studio.com</div>

<h3 class="abs footer-head" style="left:830px">NEWSLETTER SIGN UP</h3>
<p class="abs news-text">Subscribe to receive update, acces to exclusive offer and more</p>
<div class="abs news-input">Email</div>
<a class="abs subscribe-btn">Subscribe</a>
<div class="abs social" style="left:959px" aria-label="Social link"></div>
<div class="abs social" style="left:1023px" aria-label="Social link"></div>
<div class="abs social" style="left:1083px" aria-label="Social link"></div>

<div class="abs footer-line"></div>
<p class="abs copyright">© COPYRIGHT 2024 Company Name| All Rights Reserved</p>

</body>
</html>
```